Flyer-Design für ein Montessori Familienzentrum
Super Zusammenarbeit :) Meine Wünsche und Ideen wurden sehr passend und schnell umgesetzt und miteinbezogen in das Design.
Zielgruppe
Wir sind ein Montessori Familienzentrum mit folgendem Angebot:
- Montessori Eltern-Kind-Gruppen für Babys ab 8 Wochen - 4 Jahren
- Montessori Coaching
- Stoffwindel- und Windelfrei Beratung
- Beratung zur Babygeleiteten Beikost
- Workshops für Eltern
Aufgabenstellung
Schlicht, Informativ, Überblick über die Angebote

```html
<!DOCTYPE html>
<html lang="de">
<head>
<meta charset="utf-8">
<title>WaldWichtel – Montessori Familienzentrum Flyer</title>
<link href="https://fonts.googleapis.com/css2?family=Barlow+Condensed:ital,wght@0,300;0,400;1,300;1,400&family=Dosis:wght@400;500&family=Titillium+Web:ital,wght@1,700&family=Playfair+Display:wght@700&family=Great+Vibes&display=swap" rel="stylesheet">
<style>
:root{
  --frame:#a3a2a3;
  --paper:#ffffff;
  --wash:#efefef;
  --orange:#e8782f;
  --green:#3e7a2c;
  --ink:#4d4d4d;
  --ink-soft:#6a6a6a;
}
*{margin:0;padding:0;box-sizing:border-box}
html,body{width:1200px;height:828px;overflow:hidden;background:var(--frame)}
.canvas{position:relative;width:1200px;height:828px}
.spread{position:absolute;left:14px;width:1171px;height:390px;background:var(--paper);overflow:hidden}
.spread--outside{top:17px}
.spread--inside{top:419px}
.wash{position:absolute;inset:0}
.abs{position:absolute;z-index:2}
.photo{position:absolute;z-index:1}
.body{font-family:"Barlow Condensed",sans-serif;font-weight:300;font-size:6.6px;line-height:8.8px;color:var(--ink);text-align:justify}
.headline{font-family:"Titillium Web",sans-serif;font-style:italic;font-weight:700;color:var(--orange);font-size:17px;line-height:20px}
.subhead{font-family:"Barlow Condensed",sans-serif;font-style:italic;font-weight:300;color:var(--ink);font-size:11px}
.caps{font-family:"Dosis",sans-serif;font-weight:400;color:var(--green);font-size:13px;letter-spacing:.3px;line-height:14px}
.caps-sub{font-family:"Barlow Condensed",sans-serif;font-style:italic;font-weight:300;color:var(--orange);font-size:9px}
.bullets{list-style:none;font-family:"Barlow Condensed",sans-serif;font-weight:300;font-size:6.8px;line-height:8.8px;color:var(--ink)}
.bullets li::before{content:"• "}
.brand{position:absolute;z-index:2;display:flex;flex-direction:column;align-items:center;justify-content:center;border:1.5px solid var(--green);border-radius:50%;font-family:"Dosis",sans-serif;font-weight:500;color:var(--green);text-align:center}
.tagline{font-family:"Dosis",sans-serif;font-size:7.4px;letter-spacing:1.1px;color:var(--ink)}
</style>
</head>
<body>
<div class="canvas">

<!-- OUTSIDE SPREAD -->
<section class="spread spread--outside">
  <svg class="wash" viewBox="0 0 1171 390" preserveAspectRatio="none">
    <polygon points="0,180 390,10 390,330 0,390" fill="var(--wash)"/>
    <polygon points="390,10 780,180 780,390 390,390" fill="var(--wash)"/>
    <polygon points="780,180 1171,20 1171,240 780,390" fill="var(--wash)"/>
  </svg>

  <!-- Panel: Beratung -->
  <div class="photo" role="img" aria-label="Holztablett mit bunten Stoffwindeln" style="left:108px;top:0;width:278px;height:160px;background:linear-gradient(135deg,#e9e4dc,#7fb34a 45%,#3f6fb0 70%,#d8d2c6);border-radius:10px 10px 40px 10px;opacity:.9"></div>
  <h2 class="headline abs" style="left:12px;top:168px">Weiter Beratungsangebote:</h2>
  <div class="subhead abs" style="left:70px;top:193px">Stoffwindel– und Windelfrei-Beratung:</div>
  <p class="body abs" style="left:70px;top:209px;width:170px">Für alle Eltern, die sich für das Thema Stoffwindeln und Abhalten interessierenund gern mehr darüber erfahren möchten. Auch für (Stoff)-Eltern, die Probleme haben oder etwas Neues ausprobieren wollen.</p>
  <ul class="bullets abs" style="left:84px;top:247px">
    <li>Einzel- Paarberatung</li><li>Workshops</li><li>Stoffwindelparty</li><li>Problemanalysen</li><li>Miet- und Testpakete (ab Geburt – Trocken werden)</li>
  </ul>
  <div class="photo" role="img" aria-label="Tablett mit Stoffwindel und Pflegedose" style="left:0;top:296px;width:140px;height:94px;background:linear-gradient(160deg,#c33a32,#e8d6c8 55%,#f4f4f4);border-radius:0 30px 0 0"></div>
  <div class="subhead abs" style="left:195px;top:307px;line-height:13px">Beratung rund ums Thema:<br>Babygeleitete Beikost</div>
  <p class="body abs" style="left:195px;top:336px;width:170px">Du möchtest wissen, was genau BLW ist und wie man es am besten umsetzt? Oder setzt es schon um, kommst aber nicht weiter? Dann ist eine individuelle Beratung genau das Richtige!</p>
  <ul class="bullets abs" style="left:210px;top:366px"><li>Einzelberatungen</li><li>Workshops</li></ul>

  <!-- Panel: Über mich -->
  <p class="body abs" style="left:416px;top:49px;width:160px">Hallo,<br>mein Name ist Lena, ich bin Jahrgang 1994, verheiratet und wohne mit meiner Familie in Lindenau. Ich bin staatlich anerkannte Erzieherin und habe nach meiner Ausbildungszeit zunächst ein Jahr in Amerika gelebt und gearbeitet und danach in einer normalen und einer integrativen Kinderkrippe. Die WaldWichtel habe ich im September 2020 gegründet und seit September 2021 hat das Kurskonzept einen Montessori Schwerpunkt.<br>Neben meiner Fortbildung zur Montessori Spielgruppenleiterin bei Clara Berger und zahlreichen Fortbildungen zum Montessori Kinderhaus Material, mache ich derzeit noch zusätzlich mein Montessori Diplom für Kleinkinder an der Montessori Akademie in Salzburg. Ich bin außerdem zertifizierte Stoffwindelberaterin, Windelfrei Coach und Fachkraft für Babygeleitet Beikost (BLW).<br>Ich freue mich Euch in einem meiner Kurse kennenzulernen.</p>
  <div class="abs" style="left:495px;top:212px;font-family:'Great Vibes',cursive;font-size:17px;color:var(--ink)">Eure Lena</div>
  <div class="photo" role="img" aria-label="Familienfoto auf einer Wiese: Mutter, Vater und Kleinkind" style="left:609px;top:0;width:172px;height:274px;background:linear-gradient(180deg,#c9bfcb,#9a7c66 45%,#6b4b36);border-radius:0 0 86px 86px / 0 0 100px 100px"></div>
  <div class="brand" style="left:472px;top:290px;width:84px;height:84px;font-size:12px">WaldWichtel</div>
  <div class="abs" style="left:573px;top:292px;font-family:'Dosis',sans-serif;font-size:15px;letter-spacing:.8px;color:var(--ink)">LENA HARTMANN</div>
  <p class="abs" style="left:608px;top:316px;font-family:'Barlow Condensed',sans-serif;font-style:italic;font-weight:300;font-size:7.4px;line-height:10px;color:var(--ink);text-align:center;width:104px">Staatlich anerkannte Erzieherin -<br>Diplom Montessori Pädagogin i.A.<br>zertifizierte Stoffwindelberaterin /<br>Abhalte- und Windelfrei Coach,<br>Fachkraft für Babygeleitete Beikost</p>

  <!-- Panel: Titel -->
  <div class="brand" style="left:797px;top:18px;width:82px;height:82px;font-size:12px">WaldWichtel</div>
  <div class="photo" role="img" aria-label="Hände halten eine Papierkette einer Familie" style="left:900px;top:0;width:271px;height:318px;background:radial-gradient(ellipse at 55% 45%,#f1c7ad,#d8957a 60%,#f7f7f7 95%);clip-path:polygon(0 0,100% 0,100% 100%,40% 100%,30% 82%,0 55%)"></div>
  <h1 class="abs" style="left:818px;top:264px;font-family:'Playfair Display',serif;font-weight:700;font-size:29px;line-height:30px;color:var(--green);letter-spacing:.5px">MONTESSORI</h1>
  <div class="abs" style="left:818px;top:291px;font-family:'Playfair Display',serif;font-size:23px;color:var(--green);letter-spacing:1px">Familienzentrum</div>
  <div class="tagline abs" style="left:819px;top:322px">MONTESSORI PÄDAGOGIK FÜR BABYS UND KLEINKINDER</div>
  <div class="abs" style="left:977px;top:339px;font-family:'Dosis',sans-serif;font-size:7.6px;letter-spacing:1px;color:var(--orange)">AB 8 WOCHEN BIS 4 JAHRE</div>
  <div class="abs" style="left:826px;top:373px;font-family:'Dosis',sans-serif;font-size:6px;letter-spacing:.5px;color:var(--ink)">INFO@WALDWICHTEL.DE &nbsp; WWW.WALDWICHTEL.DE &nbsp; WALDWICHTEL &nbsp; WALDWICHTEL</div>
</section>

<!-- INSIDE SPREAD -->
<section class="spread spread--inside">
  <svg class="wash" viewBox="0 0 1171 390" preserveAspectRatio="none">
    <polygon points="0,170 390,30 390,280 0,250" fill="var(--wash)"/>
    <polygon points="90,300 390,170 390,390 60,390" fill="var(--wash)"/>
    <polygon points="390,20 780,150 780,390 390,300" fill="var(--wash)"/>
    <polygon points="780,160 1171,60 1171,290 780,390" fill="var(--wash)"/>
  </svg>

  <!-- Panel: Spielgruppen -->
  <h2 class="headline abs" style="left:12px;top:20px">Spielgruppen für Babys</h2>
  <div class="subhead abs" style="left:114px;top:40px">Ab 8 Wochen – 4 Jahre</div>
  <div class="caps abs" style="left:20px;top:84px">WAS IST MONTESSORI?</div>
  <div class="caps-sub abs" style="left:69px;top:97px">Informationen zum pädagogischen Konzept</div>
  <p class="body abs" style="left:20px;top:112px;width:174px">In den Gruppenstunden liegt der Schwerpunkt auf der Beobachtung seines eigenen Kindes und der Eltern-Kind-Beziehung. Jedes Kind gestaltet seine Zeit ganz individuell nach seinen Bedürfnissen. Jede Gruppe hat einen individuell gestalteten Gruppenraum mit Montessori Material aus der Altersgruppe 0-3 Jahren sowie 3-6 Jahren.</p>
  <div class="caps abs" style="left:20px;top:188px">UMSETZUNG ZUHAUSE</div>
  <div class="caps-sub abs" style="left:130px;top:201px">Anleitung der Eltern</div>
  <p class="body abs" style="left:20px;top:216px;width:174px">Zu jedem Thema bekommen die Eltern Unterstützung und Hilfestellung zur Umsetzung zu Hause. Im Elternportal der Website finden sie außerdem zusätzliche Tipps und Tricks.</p>
  <div class="photo" role="img" aria-label="Mutter mit Baby auf dem Arm im Herbstlicht" style="left:226px;top:0;width:164px;height:258px;background:linear-gradient(160deg,#c8a56b,#8a4d2e 55%,#efe7df);border-radius:40px 0 0 90px / 60px 0 0 120px"></div>
  <div class="photo" role="img" aria-label="Kindergeburtstag im Freien mit Luftballons" style="left:0;top:258px;width:157px;height:132px;background:linear-gradient(170deg,#9fc27a,#f2a7b6 50%,#e6c35b);border-radius:0 90px 0 0 / 0 80px 0 0"></div>
  <div class="caps abs" style="left:166px;top:295px">FAMILIEN-EVENTS</div>
  <div class="caps-sub abs" style="left:210px;top:308px">Austausch und Vernetzung</div>
  <p class="body abs" style="left:166px;top:323px;width:198px">1x pro Kursblock findet ein Eltern - Event wie z.B. Eltern-Coaching, Sommerfest, Martinsumzug, etc. statt. Die Eltern können sich mit Teilnehmern aus anderen Kursen austauschen.</p>
  <div class="tagline abs" style="left:167px;top:376px">MONTESSORI PÄDAGOGIK FÜR BABYS UND KLEINKINDER</div>

  <!-- Panel: Gruppeneinteilung -->
  <h2 class="headline abs" style="left:404px;top:20px">Gruppeneinteilung</h2>
  <div class="caps abs" style="left:406px;top:64px">BABY KURSE</div>
  <div class="caps-sub abs" style="left:436px;top:76px">ab 8 Wochen bis 6 Monate</div>
  <p class="body abs" style="left:406px;top:90px;width:148px">Im Baby Kurs lernen die Teilnehmer unter anderem die verschiedenen Montessori Mobiles kennen. Wir sprechen über Themen wie z.B.: Ernährung, bedürfnisorientiertes Wickeln, Eingewöhnung in die KITA und noch vieles mehr.</p>
  <div class="caps abs" style="left:406px;top:150px">CRAWLER KURSE</div>
  <div class="caps-sub abs" style="left:436px;top:162px">ab 6 Monaten bis ca.15 Monate</div>
  <p class="body abs" style="left:406px;top:176px;width:160px">Im Crawler Kurs findet eine gemeinsame Brotzeit nach BLW statt. Ein Montessori Spiegel mit integrierter Pull-up-Stange lädt die Kinder zum Hochziehen ein. Die Kinder finden außerdem Montessori Material für ihre Altersgruppe.</p>
  <div class="caps abs" style="left:406px;top:242px">TODDLER KURSE</div>
  <div class="caps-sub abs" style="left:434px;top:254px">ab ca. 15 Monaten bis max. 36 Monate</div>
  <p class="body abs" style="left:406px;top:268px;width:194px">In den Toddler Kursen liegt der Schwerpunkt auf den Dingen des täglichen Lebens und auf der Entwicklung zur Selbständigkeit. So können sie sich selbst Essen zu bereiten, sich selbst ein Glas Wasser einschenken und noch vieles mehr.</p>
  <div class="caps abs" style="left:406px;top:317px">PRESCOOLER KURSE</div>
  <div class="caps-sub abs" style="left:436px;top:329px">ab 2 Jahren bis max. 4 Jahre</div>
  <p class="body abs" style="left:406px;top:343px;width:248px;text-align:left">Im Preschooler Kurs haben die Kinder neben den Übungen des täglichen Lebens noch zusätzlich die Möglichkeit, erste Erfahrungen mit Buchstaben und Zahlen, sowie mit Geografie-Material zu machen.</p>
  <div class="photo" role="img" aria-label="Neugeborenes Baby auf weißer Decke" style="left:572px;top:0;width:204px;height:96px;background:linear-gradient(160deg,#eae7e6,#f4d9cf 50%,#dcdcdc);border-radius:90px 0 0 0"></div>
  <div class="photo" role="img" aria-label="Krabbelndes Kleinkind im gestreiften Pulli" style="left:570px;top:97px;width:206px;height:127px;background:linear-gradient(160deg,#c7b8a4,#e9d5c6 55%,#7d98b4);border-radius:60px 0 0 60px"></div>
  <div class="photo" role="img" aria-label="Regal mit Montessori Material und Globus" style="left:604px;top:225px;width:172px;height:165px;background:linear-gradient(180deg,#e0d8ca,#b9a68a 50%,#6fa05b);clip-path:polygon(0 0,100% 0,100% 100%,104px 100%,66px 68%,30px 42%)"></div>

  <!-- Panel: Coaching -->
  <h2 class="headline abs" style="left:808px;top:18px">Montessori Coaching<br>für Zuhause</h2>
  <div class="subhead abs" style="left:857px;top:60px">Ab Babyalter - Preschool Alter</div>
  <p class="body abs" style="left:808px;top:96px;width:156px;text-align:left">Wir gestalten zusammen Euer individuelles Zuhause nach den Prinzipien der Montessori Pädagogik.</p>
  <div class="abs" style="left:808px;top:124px;font-family:'Barlow Condensed',sans-serif;font-weight:300;font-size:7px;color:var(--ink)">WIE LÄUFT EIN MONTESSORI COACHING AB?</div>
  <p class="body abs" style="left:808px;top:137px;width:156px;text-align:left">Das Coaching besteht aus 3 Hausbesuchen, die jeweils ca. 2 Stunden dauern und sich über einen Zeitraum von 6-8 Wochen erstrecken.</p>
  <div class="photo" role="img" aria-label="Weißer Kindertisch mit Körben und Tischläufer" style="left:1016px;top:0;width:155px;height:258px;background:linear-gradient(180deg,#d9d3c8,#f2efea 55%,#c6b8a0);border-radius:70px 0 0 90px / 100px 0 0 110px"></div>
  <div class="photo" role="img" aria-label="Kinder-Waschtisch aus Holz mit Wasserspender" style="left:806px;top:185px;width:190px;height:205px;background:linear-gradient(180deg,#f3f1ee,#dcc3a0 45%,#c9a879)"></div>
  <div class="brand" style="left:1040px;top:280px;width:100px;height:100px;font-size:14px">WaldWichtel</div>
</section>

</div>
</body>
</html>
```